need illustration for a landing page

creating a landing page for a launch meme coin. I need illustrations for a landing page
similar to https://brindlemark.io/ but featuring the cat and cat themed. must be a bit more serious than the chicken. check out zovatelo.com

```html
<!DOCTYPE html>
<html lang="en">
<head>
<meta charset="utf-8">
<title>Whiskora — Join the Revolution</title>
<link href="https://fonts.googleapis.com/css2?family=Outfit:wght@300;400;600;700;800&display=swap" rel="stylesheet">
<style>
  :root {
    --ink: #000000;
    --ember: #d63a00;
    --royal-blue: #0a5cff;
    --gold: #f2c200;
    --paper: #ffffff;
    --glow-amber: #b8652a;
    --glow-plum: #4a3a5c;
    --night: #12131f;
    --panel: rgba(255, 255, 255, 0.04);
  }

  * { margin: 0; padding: 0; box-sizing: border-box; }

  html, body {
    width: 1200px;
    height: 626px;
    overflow: hidden;
    background: var(--ink);
  }

  .hero {
    position: relative;
    width: 1200px;
    height: 626px;
    overflow: hidden;
    font-family: "Outfit", sans-serif;
    color: var(--paper);
    background:
      radial-gradient(ellipse 420px 360px at 1210px 600px, rgba(184, 101, 42, 0.95), rgba(184, 101, 42, 0) 100%),
      radial-gradient(ellipse 520px 300px at 1150px 330px, rgba(150, 60, 20, 0.55), rgba(150, 60, 20, 0) 100%),
      linear-gradient(162deg, rgba(0,0,0,0) 62%, rgba(74, 58, 92, 0.55) 80%, rgba(18, 19, 31, 0.2) 100%),
      linear-gradient(180deg, var(--ink) 0%, var(--ink) 70%, var(--night) 100%);
  }

  .mascot-art {
    position: absolute;
    left: 140px;
    top: 72px;
    width: 358px;
    height: 482px;
    border-radius: 48% 48% 40% 40%;
    background:
      radial-gradient(circle at 62% 8%, rgba(242, 194, 0, 0.55), rgba(242, 194, 0, 0) 28%),
      linear-gradient(90deg, rgba(214, 58, 0, 0.6) 0%, rgba(214, 58, 0, 0.25) 45%, rgba(10, 92, 255, 0.3) 60%, rgba(10, 92, 255, 0.6) 100%);
  }

  .pitch-panel {
    position: absolute;
    left: 604px;
    top: 77px;
    width: 472px;
    height: 472px;
    border-radius: 20px;
    background: var(--panel);
  }

  .pitch-content {
    position: absolute;
    left: 636px;
    top: 126px;
    width: 440px;
  }

  .headline {
    font-weight: 700;
    font-size: 48px;
    line-height: 43px;
    letter-spacing: -0.5px;
    text-transform: uppercase;
  }
  .headline-lead { color: var(--ember); display: block; }
  .headline-accent { color: var(--royal-blue); display: block; }

  .tagline {
    margin-top: 26px;
    font-weight: 600;
    font-size: 16px;
    letter-spacing: -0.1px;
  }

  .description {
    margin-top: 20px;
    width: 420px;
    font-weight: 300;
    font-size: 16.6px;
    line-height: 24.4px;
  }

  .cta-button {
    display: inline-flex;
    align-items: center;
    justify-content: center;
    margin-top: 20px;
    margin-left: 4px;
    width: 229px;
    height: 48px;
    border: 2px solid var(--royal-blue);
    color: var(--paper);
    font-weight: 700;
    font-size: 22px;
    letter-spacing: 0.5px;
    text-decoration: none;
    text-transform: uppercase;
  }
</style>
</head>
<body>
  <main class="hero">
    <div class="mascot-art" role="img" aria-label="Illustration of a crowned cat head drawn in orange and blue line strokes with golden eyes"></div>

    <div class="pitch-panel"></div>

    <section class="pitch-content">
      <h1 class="headline">
        <span class="headline-lead">Join the</span>
        <span class="headline-accent">Revolution</span>
      </h1>
      <p class="tagline">Whiskora (WSKR$): The Future of Feline Finance</p>
      <p class="description">Whiskora (WSKR$) is a meme-driven cryptocurrency with claws. Inspired by the resilience and independence of cat lovers everywhere, Whiskora is more than just a joke—it’s a movement. Built on a foundation of humor, social commentary, and financial empowerment, Whiskora takes on the world with the cunning of a cat queen.</p>
      <a class="cta-button" href="#">Get Started</a>
    </section>
  </main>
</body>
</html>
```